Hi, everyone!

We're looking for a tenacious designer to help us create two (2) 33 x 86 single-sided retractable banners. The banners will be purchased through
Bannerloft (see: https://www.bannerloft-example.ca/signs-posters/retractable-banners?xnav=swsProductOnly_ResultTitle).

I have attached a wide variety of materials including the Plovrix - Creative Production logos (.psd files), previous attempts at making a banner including some handwritten notes and a table cloth that will be used in the same space as the banners and the back of our business card to give you an idea of our colours.

Note: We like the colours used on the other banner designs but do not like the layout or icons - they look cluttered and unprofessional. They are good as a guide but not what we want as a design. Similarly, avoid featuring close-ups of people from stock photos.

At least one of the banners must feature: (you can use icons instead of words if it means a better design)

www.plovrix-example.ca
Email: get@plovrix-example.ca
Phone: (555) 214-0873
Social Media Handle: plovrixstudio

There is also a word document on the bottom to guide some of the copywriting that may be used. If you're really ambitious, we're happy to consider different phrases and copy.

Finally, the fonts that we use are:
Plovrix Logo - Metropolis
Titles: Adelle Font Family
Body / Content: Avenir Font Family

As with everything, we welcome other suggestions or recommendations.

Target Market(s)

Government, Small Business, Non-Profits, Indigenous Canadian Communities

Font styles to use
Sans Serif

Colors

Designer to choose colors to be used in the design.

Requirements
Must have
• The deliverables for this project are:
• - Two (2) 33 x 86 Single-Sided Retractable Banners
• They will be purchased through Bannerloft Canada (see: https://www.bannerloft-example.ca/signs-posters/retractable-banners?xnav=swsProductOnly_ResultTitle). You may want to try loading your design there before submitting them to us.
Nice to have
• We like the colours of the initial designs but they are unprofessional, cluttered and from a template. Ideally, we would like a unique design that works with the colours in our logo (red, black, white and yellow).
• One banner may focus on Tourism Development and the other could feature Creative Strategy.
Should not have
• Please do not use stock photos that feature people - our target market is put off by such pictures. If you'd like an idea of our tourism focus, visit:
• - https://northwoodtravelcircle-example.ca/en/
• - https://lakeheadjourneys-example.ca/
• - https://www.qolfa-example.org/

```html
<!DOCTYPE html>
<html lang="en">
<head>
<meta charset="utf-8">
<title>Plovrix Retractable Banners</title>
<link href="https://fonts.googleapis.com/css2?family=Catamaran:wght@500;600;700;800&family=Mulish:wght@400;500;600&display=swap" rel="stylesheet">
<style>
  :root {
    --red: #c21f2f;
    --yellow: #f0b323;
    --charcoal: #303135;
    --white: #ffffff;
    --ink: #1b1b1d;
    --stage-top: #c9cbc4;
    --stage-bottom: #e6e7e2;
  }
  * { box-sizing: border-box; margin: 0; padding: 0; }
  html, body { width: 1200px; height: 1200px; overflow: hidden; }
  body {
    background: linear-gradient(180deg, var(--stage-top), var(--stage-bottom));
    font-family: "Mulish", sans-serif;
    position: relative;
  }
  .banner {
    position: absolute;
    top: 105px;
    width: 380px;
    height: 990px;
    background: var(--charcoal);
    overflow: hidden;
    box-shadow: 0 12px 30px rgba(0,0,0,0.18);
  }
  .banner--strategy { left: 160px; }
  .banner--tourism { left: 660px; }

  .banner__topband { height: 12px; background: var(--red); }
  .banner__header {
    height: 128px;
    background: var(--white);
    display: flex;
    align-items: center;
    justify-content: center;
    gap: 12px;
  }
  .brand__dot { width: 22px; height: 22px; border-radius: 50%; background: var(--red); }
  .brand__name {
    font-family: "Catamaran", sans-serif;
    font-weight: 800;
    font-size: 54px;
    letter-spacing: 1px;
    color: var(--ink);
    line-height: 1;
  }

  .banner__body { padding: 22px 32px 0 38px; color: var(--white); }
  .headline {
    font-family: "Catamaran", sans-serif;
    font-weight: 800;
    color: var(--yellow);
    line-height: 1.1;
  }
  .banner--strategy .headline { font-size: 34px; }
  .banner--tourism .headline { font-size: 30px; }
  .subhead {
    font-family: "Catamaran", sans-serif;
    font-weight: 500;
    font-size: 22px;
    line-height: 1.2;
    margin-top: 8px;
  }
  .subhead em { color: var(--yellow); font-style: italic; }
  .rule { height: 3px; background: var(--yellow); margin: 12px 0 14px; }
  .copy { font-size: 12px; line-height: 1.45; text-align: justify; }
  .copy--small { font-size: 10px; }
  .section-title {
    font-family: "Catamaran", sans-serif;
    font-weight: 800;
    font-size: 22px;
    color: var(--yellow);
    margin-top: 22px;
  }
  .services { list-style: none; margin-top: 6px; }
  .services li {
    font-family: "Catamaran", sans-serif;
    font-weight: 500;
    font-size: 16px;
    line-height: 1.45;
    padding-left: 14px;
    position: relative;
  }
  .services li::before {
    content: "";
    position: absolute;
    left: 0; top: 8px;
    border-left: 7px solid var(--yellow);
    border-top: 4.5px solid transparent;
    border-bottom: 4.5px solid transparent;
  }
  .location { font-size: 10px; line-height: 1.45; text-align: justify; }

  .approach-title { text-align: center; }
  .approach {
    display: grid;
    grid-template-columns: repeat(4, 1fr);
    gap: 6px;
    margin: 14px -14px 0 -18px;
    text-align: center;
  }
  .approach__icon {
    width: 58px; height: 58px;
    border-radius: 50%;
    background: var(--red);
    border: 2px solid var(--charcoal);
    box-shadow: 0 0 0 1.5px var(--yellow);
    margin: 0 auto;
    display: flex; align-items: center; justify-content: center;
  }
  .approach__label {
    font-family: "Catamaran", sans-serif;
    font-weight: 800;
    font-size: 12px;
    color: var(--yellow);
    margin-top: 8px;
    letter-spacing: 0.3px;
  }
  .approach__text { font-size: 7.5px; line-height: 1.35; margin-top: 2px; }

  .banner__photo {
    position: absolute;
    left: 0; top: 715px;
    width: 380px; height: 205px;
  }
  .banner__footer {
    position: absolute;
    left: 0; bottom: 0;
    width: 100%; height: 82px;
    background: var(--red);
    display: flex; flex-direction: column;
    align-items: center; justify-content: center;
    gap: 6px;
    font-family: "Catamaran", sans-serif;
    font-weight: 600;
    font-size: 14px;
    color: var(--white);
  }
  .contact-row { display: flex; align-items: center; gap: 8px; line-height: 1; }
  .contact-row .sep { color: var(--yellow); }
  .contact-item { display: inline-flex; align-items: center; gap: 5px; }
  .contact-icon { width: 12px; height: 12px; flex: none; }
  .social-mark {
    width: 12px; height: 12px;
    border-radius: 2px;
    background: var(--yellow);
    flex: none;
  }
</style>
</head>
<body>

<section class="banner banner--strategy">
  <div class="banner__topband"></div>
  <header class="banner__header">
    <span class="brand__dot"></span>
    <span class="brand__name">PLOVRIX</span>
  </header>
  <div class="banner__body">
    <h1 class="headline">Creative,<br>Culturally<br>Inspired Strategy</h1>
    <p class="subhead">We Start with Your Story</p>
    <div class="rule"></div>
    <p class="copy">At Plovrix we start with your story. It enables us to create a deeper connection, unite people and drives meaningful growth. As your Indigenous marketing, communication and event partner, we use the power of story to learn, share, elevate and innovate.</p>
    <h2 class="section-title">How Can We Help?</h2>
    <ul class="services">
      <li>Destination and Product Development</li>
      <li>Media and Marketing</li>
      <li>Event Management and Planning</li>
      <li>Brand Development</li>
      <li>Graphic, Print and Web Design</li>
    </ul>
    <div class="rule"></div>
    <p class="location">Based in Northwestern Ontario at the foot of Animkii Wajiw (“Thunder Mountain” or “Mount McKay”) we’re ready to tell your story through our globally informed skillset tailored for meaningful and measurable local results.</p>
  </div>
  <svg class="banner__photo" viewBox="0 0 380 205" preserveAspectRatio="none" role="img" aria-label="Photo of a stone inukshuk on a golden tundra hillside above a river valley with mountains and blue sky">
    <defs>
      <linearGradient id="tundra" x1="0" y1="0" x2="0" y2="1">
        <stop offset="0" stop-color="#b9d3ea"/>
        <stop offset="0.35" stop-color="#8aa7bf"/>
        <stop offset="0.6" stop-color="#9a9a6a"/>
        <stop offset="1" stop-color="#a97a46"/>
      </linearGradient>
    </defs>
    <path d="M0 32 Q190 -14 380 58 L380 205 L0 205 Z" fill="url(#tundra)"/>
    <path d="M0 28 Q190 -18 380 54" fill="none" stroke="var(--yellow)" stroke-width="9"/>
  </svg>
  <footer class="banner__footer">
    <div class="contact-row">
      <span class="contact-item">
        <svg class="contact-icon" viewBox="0 0 12 12" aria-hidden="true"><circle cx="6" cy="6" r="5" fill="none" stroke="var(--yellow)" stroke-width="1.4"/><path d="M1 6 H11 M6 1 Q3 6 6 11 M6 1 Q9 6 6 11" fill="none" stroke="var(--yellow)" stroke-width="1"/></svg>
        plovrix-example.live/tourism</span>
      <span class="sep">|</span>
      <span class="contact-item">
        <svg class="contact-icon" viewBox="0 0 12 12" aria-hidden="true"><rect x="1" y="2.5" width="10" height="7" rx="1" fill="var(--yellow)"/><path d="M1.5 3 L6 6.5 L10.5 3" fill="none" stroke="var(--red)" stroke-width="1"/></svg>
        get@plovrix-example.ca</span>
    </div>
    <div class="contact-row">
      <span class="contact-item">
        <svg class="contact-icon" viewBox="0 0 12 12" aria-hidden="true"><path d="M2.5 1 L4.5 1 L5.5 3.5 L4.2 4.6 Q5.2 6.8 7.4 7.8 L8.5 6.5 L11 7.5 L11 9.5 Q11 11 9.5 11 Q1 10.5 1 2.5 Q1 1 2.5 1 Z" fill="var(--yellow)"/></svg>
        (555) 214-0873</span>
      <span class="sep">|</span>
      <span class="contact-item"><span class="social-mark"></span>plovrixstudio</span>
    </div>
  </footer>
</section>

<section class="banner banner--tourism">
  <div class="banner__topband"></div>
  <header class="banner__header">
    <span class="brand__dot"></span>
    <span class="brand__name">PLOVRIX</span>
  </header>
  <div class="banner__body">
    <h1 class="headline">Creating Meaningful Experiences through Problem-Solving</h1>
    <p class="subhead">Redefining <em>Plovrixment</em> for Real Outcomes</p>
    <div class="rule"></div>
    <p class="copy copy--small">Our context informs our needs. Our experience and backgrounds in tourism and community development, outdoor recreation, marketing, film production, project management and design ensure those needs are met. Our services are</p>
    <h2 class="section-title approach-title">Our Approach</h2>
    <div class="approach">
      <div class="approach__step">
        <div class="approach__icon">
          <svg width="30" height="30" viewBox="0 0 30 30" aria-hidden="true"><circle cx="12" cy="12" r="7" fill="none" stroke="var(--yellow)" stroke-width="2.5"/><path d="M17 17 L25 25" stroke="var(--yellow)" stroke-width="4" stroke-linecap="round"/></svg>
        </div>
        <div class="approach__label">DISCOVER</div>
        <p class="approach__text">We’re adventurers at heart. Our inquisitive nature, cultural knowledge and perspective allows us to understand a challenge and find a suitable solution</p>
      </div>
      <div class="approach__step">
        <div class="approach__icon">
          <svg width="30" height="30" viewBox="0 0 30 30" aria-hidden="true"><path d="M24 15 A9 9 0 1 1 15 6" fill="none" stroke="var(--yellow)" stroke-width="2.5"/><path d="M12 18 L22 8 L24 10 L14 20 L11 21 Z" fill="var(--yellow)"/></svg>
        </div>
        <div class="approach__label">DEFINE</div>
        <p class="approach__text">Our company comes from a desire to create real outcomes. We work to understand the challenges and opportunities that real people encounter in their lives.</p>
      </div>
      <div class="approach__step">
        <div class="approach__icon">
          <svg width="30" height="30" viewBox="0 0 30 30" aria-hidden="true"><path d="M6 6 L24 24 M24 6 L6 24" stroke="var(--yellow)" stroke-width="3.5" stroke-linecap="round"/></svg>
        </div>
        <div class="approach__label">DESIGN</div>
        <p class="approach__text">Opportunities understanding of observed, human need. The services we provided are all focused on meaningful and useful experiences for people.</p>
      </div>
      <div class="approach__step">
        <div class="approach__icon">
          <svg width="32" height="30" viewBox="0 0 32 30" aria-hidden="true"><rect x="3" y="8" width="17" height="13" rx="2" fill="var(--yellow)"/><path d="M20 12 H26 L29 17 V21 H20 Z" fill="var(--yellow)"/><circle cx="9" cy="23" r="3" fill="var(--yellow)" stroke="var(--red)" stroke-width="1.5"/><circle cx="24" cy="23" r="3" fill="var(--yellow)" stroke="var(--red)" stroke-width="1.5"/></svg>
        </div>
        <div class="approach__label">DELIVER</div>
        <p class="approach__text">We provide services across the entire customer journey. Our services all present an opportunity to learn more and build on</p>
      </div>
    </div>
  </div>
  <svg class="banner__photo" viewBox="0 0 380 205" preserveAspectRatio="none" role="img" aria-label="Photo of a large waterfall with rising mist above a blue river and a tour boat">
    <defs>
      <linearGradient id="falls" x1="0" y1="0" x2="0" y2="1">
        <stop offset="0" stop-color="#c7dde4"/>
        <stop offset="0.4" stop-color="#e6f1f3"/>
        <stop offset="0.7" stop-color="#6fb0cc"/>
        <stop offset="1" stop-color="#2e7ea6"/>
      </linearGradient>
    </defs>
    <path d="M0 48 Q170 -14 380 30 L380 205 L0 205 Z" fill="url(#falls)"/>
    <path d="M0 44 Q170 -18 380 26" fill="none" stroke="var(--yellow)" stroke-width="9"/>
  </svg>
  <footer class="banner__footer">
    <div class="contact-row">
      <span class="contact-item">
        <svg class="contact-icon" viewBox="0 0 12 12" aria-hidden="true"><circle cx="6" cy="6" r="5" fill="none" stroke="var(--yellow)" stroke-width="1.4"/><path d="M1 6 H11 M6 1 Q3 6 6 11 M6 1 Q9 6 6 11" fill="none" stroke="var(--yellow)" stroke-width="1"/></svg>
        plovrix-example.live/tourism</span>
      <span class="sep">|</span>
      <span class="contact-item">
        <svg class="contact-icon" viewBox="0 0 12 12" aria-hidden="true"><rect x="1" y="2.5" width="10" height="7" rx="1" fill="var(--yellow)"/><path d="M1.5 3 L6 6.5 L10.5 3" fill="none" stroke="var(--red)" stroke-width="1"/></svg>
        get@plovrix-example.ca</span>
    </div>
    <div class="contact-row">
      <span class="contact-item">
        <svg class="contact-icon" viewBox="0 0 12 12" aria-hidden="true"><path d="M2.5 1 L4.5 1 L5.5 3.5 L4.2 4.6 Q5.2 6.8 7.4 7.8 L8.5 6.5 L11 7.5 L11 9.5 Q11 11 9.5 11 Q1 10.5 1 2.5 Q1 1 2.5 1 Z" fill="var(--yellow)"/></svg>
        (555) 214-0873</span>
      <span class="sep">|</span>
      <span class="contact-item"><span class="social-mark"></span>plovrixstudio</span>
    </div>
  </footer>
</section>

</body>
</html>
```